I need a flyer that is professional, advertises and informs people about my health coaching practice. I am a Nationally Board Certified Health and Wellness Coach, lifestyle medicine certified and a lifestyle coach for the NBO's Glucose Readiness Program. I have my Master's Degree in Counseling Psychology. The final design should communicate evidence based health coaching that is self-directed and aimed at creating lasting health behavioral changes designed to enhance well-being. I am very open in terms of design but really would like a professional look to the flyer. I did want my contact information on the flyer: mabel@vitalgroveworks.com and (217) 586-3914

Target Market(s)

Adults looking to improve their health, decrease risk factors for lifestyle disease, reduce weight, make better lifestyle choices to improve well-being.

Industry/Entity Type

Health And Wellness

Font styles to use
Sans Serif

Colors

Designer to choose colors to be used in the design.

Requirements
Must have
• Services offered, a professional feel, Mabel Harlow Health Coaching (name of my practice), my phone number (217) 586-3914 and email: mabel@vitalgroveworks.com, location: 1873 W Larkspur Street Bloomington IL 61709 my website: mabelharlow.com to schedule appointments
Nice to have
• What is Health Coaching? Health and Wellness Coaches partner with clients seeking self-directed, lasting changes, aligned with their values, which promote health and wellness and, thereby, enhance well-being. In the course of their work health and wellness coaches display unconditional positive regard for their clients and a belief in their capacity for change, and honoring that each client is an expert on his or her life, while ensuring that all interactions are respectful and non-judgmental.

```html
<!DOCTYPE html>
<html lang="en">
<head>
<meta charset="utf-8">
<title>Mabel Harlow Health Coaching</title>
<link rel="stylesheet" href="https://fonts.googleapis.com/css2?family=Arvo:wght@400;700&family=Source+Sans+3:ital,wght@0,400;1,700;1,800&display=swap">
<style>
  :root {
    --navy: #0d5b7e;
    --band: #0e5f82;
    --teal: #4fa9c0;
    --teal-light: #3fa6bf;
    --ink-teal: #1c5a78;
    --white: #ffffff;
    --water-1: #e6f4f7;
    --water-2: #7fcfdc;
    --water-3: #3fb5c9;
  }
  * { margin: 0; padding: 0; box-sizing: border-box; }
  html, body { width: 1041px; height: 1200px; overflow: hidden; background: var(--white); }
  .flyer { position: relative; width: 1041px; height: 1200px; overflow: hidden; background: var(--white); font-family: "Source Sans 3", sans-serif; }
  .backdrop { position: absolute; left: 0; top: 0; width: 1041px; height: 1200px; }
  .headline {
    position: absolute; left: 0; top: 32px; width: 1041px; text-align: center;
    font-family: "Arvo", serif; font-weight: 700; font-size: 64px; line-height: 68px; color: var(--navy);
  }
  .intro { position: absolute; left: 75px; top: 214px; width: 388px; }
  .intro-title { font-family: "Arvo", serif; font-size: 24px; color: var(--teal-light); margin-bottom: 14px; font-weight: 400; }
  .intro-text { font-size: 16.4px; line-height: 21.7px; color: var(--ink-teal); text-align: justify; }
  .service {
    position: absolute; width: 376px; height: 180px; border-radius: 50%;
    background: var(--teal); color: var(--white);
    display: flex; flex-direction: column; align-items: center; justify-content: center; text-align: center;
    font-family: "Arvo", serif;
  }
  .service-name { font-size: 34px; line-height: 38px; font-weight: 400; }
  .service-meta { margin-top: 10px; font-size: 19px; font-weight: 700; color: var(--ink-teal); }
  .service-consult { left: 563px; top: 195px; }
  .service-data { left: 563px; top: 400px; }
  .service-single { left: 102px; top: 550px; }
  .service-package { left: 563px; top: 612px; }
  .book-band { position: absolute; left: 521px; top: 843px; width: 520px; height: 61px; }
  .book-label {
    position: absolute; left: 540px; top: 843px; width: 450px; height: 61px; line-height: 61px; text-align: center;
    font-style: italic; font-weight: 800; font-size: 42px; color: var(--white); letter-spacing: 0.5px;
  }
  .contact { position: absolute; left: 520px; top: 914px; width: 470px; text-align: center; color: var(--navy); }
  .contact-phone { font-style: italic; font-weight: 800; font-size: 47px; line-height: 56px; }
  .contact-email { font-size: 20px; line-height: 24px; }
  .contact-rule { margin: 20px auto 12px; width: 470px; height: 2px; background: var(--white); }
  .practice-name { font-family: "Arvo", serif; font-size: 25px; line-height: 32px; }
  .practice-address { font-size: 20px; line-height: 30px; margin-top: 4px; }
  .practice-site { font-size: 20px; line-height: 26px; letter-spacing: 5px; }
</style>
</head>
<body>
<main class="flyer">
  <svg class="backdrop" width="1041" height="1200" viewBox="0 0 1041 1200">
    <defs>
      <linearGradient id="waterGradient" x1="0" y1="0" x2="1" y2="0.3">
        <stop offset="0" stop-color="#f4f7f7"/>
        <stop offset="0.45" stop-color="#eef4f2"/>
        <stop offset="0.6" stop-color="#a9dfe8"/>
        <stop offset="1" stop-color="#3fb5c9"/>
      </linearGradient>
    </defs>
    <polygon role="img" aria-label="Photo of white chrysanthemum blossoms over soft turquoise water" points="0,640 1041,776 1041,1200 0,1200" fill="url(#waterGradient)"/>
  </svg>

  <h1 class="headline">Health Coaching is<br>Embracing Your Health</h1>

  <section class="intro">
    <h2 class="intro-title">What is Health Coaching?</h2>
    <p class="intro-text">Health and Wellness Coaches partner with clients seeking self-directed, lasting changes, aligned with their values, which promote health and wellness and, thereby, enhance well-being. In the course of their work health and wellness coaches display unconditional positive regard for their clients and a belief in their capacity for change, and honoring that each client is an expert on his or her life, while ensuring that all interactions are respectful and non-judgmental.</p>
  </section>

  <div class="service service-consult">
    <div class="service-name">Health Coaching<br>Initial Consultation</div>
    <div class="service-meta">30 min | Free</div>
  </div>
  <div class="service service-data">
    <div class="service-name">Health Coaching<br>Data Collection</div>
    <div class="service-meta">1 hr | $199</div>
  </div>
  <div class="service service-single">
    <div class="service-name">Individual Health<br>Coaching Session</div>
    <div class="service-meta">30 min | $50</div>
  </div>
  <div class="service service-package">
    <div class="service-name">Health Coaching<br>6 Session Package</div>
    <div class="service-meta">6 x 30 min | $275</div>
  </div>

  <svg class="book-band" width="520" height="61" viewBox="0 0 520 61">
    <polygon points="22,0 520,0 520,61 0,61" fill="var(--band)"/>
  </svg>
  <div class="book-label">BOOK NOW!</div>

  <address class="contact" style="font-style:normal">
    <div class="contact-phone">(217) 586-3914</div>
    <div class="contact-email">mabel@vitalgroveworks.com</div>
    <div class="contact-rule"></div>
    <div class="practice-name">Mabel Harlow Health Coaching</div>
    <div class="practice-address">1873 W Larkspur Street Bloomington IL 61709</div>
    <div class="practice-site">mabelharlow.com</div>
  </address>
</main>
</body>
</html>
```